Professional .net software engineer needs website design

I'm looking for someone that can design my website. The final design should fit my existing logo. You are allowed to change the color scheme, but only when you also change the colors in the psd file of my logo.

I have been a professional .net software engineer for 10 years. I focus mainly on businesses. My specialty is the development and management of complex web applications and related technologies. I'm a certified Scrum Master with hands on expierience, so I can guide a software project based on agile practises as well.

Because of my background in privacy and information security, i'm used to develop software with high quality and security standards. This is a unique selling point, because most of my fellow developers don't know and/or care about quality and security.

The final design should:

1. attract new customers and projects
2. showcase recent projects
3. showcase certifications and skills
4. fit to the "look and feel" of my existing logo

and my products and services (hosted website, technical screening of candidates, email hosting, etc.).

Target Market(s)

Businesses that:
1. require (temporary) extra development resources
2. would like to outsource their project
3. require technical screening of candidates (employment agencies)
4. agile project management consultancy

Industry/Entity Type

Computer Software

Coding

Coded - Design and coding required

Number of Pages Required

4 page

Font styles to use
Sans Serif

Requirements
Must have
• - The design should match with the look and feel of my existing logo.
• - Provide a easy way for customers to get in contact with me.
• - My experience, certifications and skills must be visible to visitors
• The menu must contain the following items:
• Home
• Projects
• About me
• Products & Services
• The design must be responsive
Nice to have
• I like dark colors like this:
• http://www.brinklomart.com/entry/4839217
• https://en.42blotners.nl/paper-kits/rounds/make-cards-sheets-wrappers-web-guard-start-730415/picks/260

```html
<!DOCTYPE html>
<html lang="en">
<head>
<meta charset="utf-8">
<title>Bright Forge — .NET Software Engineer &amp; Scrum Master</title>
<link href="https://fonts.googleapis.com/css2?family=Raleway:wght@400;500;600&family=Open+Sans:wght@400;600;700&display=swap" rel="stylesheet">
<style>
:root{
  --red:#e4242b;
  --red-dark:#c91c22;
  --ink:#333333;
  --muted:#555555;
  --line:#dddddd;
  --white:#ffffff;
  --footer:#333333;
  --hero-a:#5b6470;
  --hero-b:#2c3440;
}
*{margin:0;padding:0;box-sizing:border-box}
html,body{width:1200px;height:3383px;overflow:hidden}
body{position:relative;background:var(--white);font-family:"Open Sans",sans-serif;color:var(--ink)}
.abs{position:absolute}

/* hero */
.hero{position:absolute;left:0;top:0;width:1200px;height:620px;
  background:linear-gradient(160deg,#8a9098 0%,var(--hero-a) 40%,var(--hero-b) 100%);
  clip-path:polygon(0 0,100% 0,100% 553px,50% 620px,0 553px)}
.brand{position:absolute;left:100px;top:26px;color:var(--white)}
.brand-name{font-family:"Raleway",sans-serif;font-size:27px;font-weight:500;letter-spacing:3px;line-height:1}
.brand-tag{font-size:12px;margin-top:5px}
.nav{position:absolute;top:38px;left:428px;display:flex;gap:29px;list-style:none}
.nav li{color:var(--white);font-family:"Raleway",sans-serif;font-size:13px;letter-spacing:.5px}
.nav-rule{position:absolute;left:100px;top:99px;width:1000px;height:1px;background:rgba(255,255,255,.35)}
.hero-title{position:absolute;top:262px;width:1200px;text-align:center;color:var(--white);font-family:"Raleway",sans-serif;font-size:56px;font-weight:500;letter-spacing:6px}
.hero-sub{position:absolute;top:332px;width:1200px;text-align:center;color:var(--white);font-family:"Raleway",sans-serif;font-size:26px;font-weight:600;letter-spacing:1px}
.hero-arrow{position:absolute;top:284px}

/* generic headings */
.section-title{position:absolute;width:1200px;text-align:center;font-family:"Raleway",sans-serif;font-weight:400;color:#222;font-size:42px}
.section-sub{position:absolute;width:1200px;text-align:center;font-family:"Raleway",sans-serif;font-size:22px;color:var(--muted)}
.intro{position:absolute;left:180px;width:840px;text-align:center;font-size:11px;line-height:25px;color:var(--muted)}
.red-title{position:absolute;width:1200px;text-align:center;font-family:"Raleway",sans-serif;font-weight:600;font-size:29px;line-height:33px;color:var(--red);letter-spacing:1px}

/* experience */
.band{position:absolute;left:0}
.timeline-item{position:absolute;width:270px;color:var(--white)}
.timeline-item.left{text-align:right}
.item-title{font-family:"Raleway",sans-serif;font-size:20px;font-weight:500}
.item-role{font-size:11px;font-weight:700;margin-top:10px}
.item-text{font-size:11px;line-height:16px;margin-top:8px}
.load-more{position:absolute;left:535px;top:1703px;width:130px;height:30px;border:1px solid var(--line);border-radius:3px;
  font-size:14px;color:#999;display:flex;align-items:center;justify-content:center;gap:8px;background:var(--white)}

/* certifications */
.cert-badge{position:absolute;top:1948px;height:34px;border-radius:6px;background:#b9b9b9}

/* skills */
.skill{position:absolute;top:2258px;width:240px;text-align:center;color:var(--white)}
.skill-name{font-family:"Raleway",sans-serif;font-size:19px;margin-top:42px}
.skill-text{font-size:11px;line-height:16px;margin-top:10px;padding:0 14px}

/* contact */
.contact-item{position:absolute;top:2794px;display:flex;align-items:center;gap:14px;font-size:12px;line-height:18px;color:var(--ink)}
.contact-dot{width:32px;height:32px;border-radius:50%;background:#111;display:flex;align-items:center;justify-content:center;flex:none}
.field{position:absolute;left:214px;width:373px;height:40px;border:1px solid var(--line);font-size:10px;color:var(--muted);padding:12px 14px}
.field.message{left:609px;top:2872px;width:377px;height:196px}
.submit{position:absolute;left:503px;top:3097px;width:196px;height:46px;background:var(--red);color:var(--white);border-radius:3px;
  font-family:"Open Sans",sans-serif;font-size:18px;font-weight:600;display:flex;align-items:center;justify-content:center}

/* footer */
.footer{position:absolute;left:0;top:3147px;width:1200px;height:236px;background:var(--footer);
  clip-path:polygon(0 0,50% 56px,100% 0,100% 100%,0 100%)}
.social{position:absolute;top:3253px;left:0;width:1200px;display:flex;justify-content:center;gap:8px}
.social span{width:28px;height:28px;border-radius:50%;background:var(--white)}
.footer-nav{position:absolute;top:3302px;width:1200px;display:flex;justify-content:center;gap:12px;list-style:none;font-size:11px;color:var(--white)}
.footer-nav li+li::before{content:"/";margin-right:12px}
.copyright{position:absolute;top:3326px;width:1200px;text-align:center;font-size:11px;color:var(--white)}
</style>
</head>
<body>

<!-- hero -->
<div class="hero" role="img" aria-label="Photograph of a software engineer in a suit working on a laptop and phone, seated on outdoor stairs"></div>
<div class="brand">
  <div class="brand-name">BRIGHT FORGE</div>
  <div class="brand-tag">Analyze. Design. Build.</div>
</div>
<ul class="nav">
  <li>HOME</li><li>COMPANIES</li><li>MY EXPERIENCE</li><li>CERTIFICATIONS</li><li>SKILLS</li><li>BLOG</li><li>CONTACT</li>
</ul>
<div class="nav-rule"></div>
<svg class="hero-arrow" style="left:30px" width="30" height="50" viewBox="0 0 30 50"><polyline points="26,2 4,25 26,48" fill="none" stroke="rgba(255,255,255,.7)" stroke-width="2"/></svg>
<svg class="hero-arrow" style="left:1130px" width="30" height="50" viewBox="0 0 30 50"><polyline points="4,2 26,25 4,48" fill="none" stroke="rgba(255,255,255,.7)" stroke-width="2"/></svg>
<div class="hero-title">BRIGHT FORGE</div>
<div class="hero-sub">Professional .NET Software Engineer &amp; Scrum Master</div>

<!-- welcome -->
<h1 class="section-title" style="top:688px">Welcome To Bright Forge</h1>
<p class="section-sub" style="top:737px">I'm a certified Scrum Master</p>
<p class="intro" style="top:784px">Bright Forge builds and maintains web shops, websites and apps, and also takes care of hosting and outsourcing. With more than ten years of hands-on experience your project is in good hands. Software is built with Scrum, so you stay involved and always know what you get. Every project is delivered on time and on budget, guarded by an experienced certified Scrum Master.</p>

<!-- experience -->
<svg class="band" style="top:932px" width="1200" height="742" viewBox="0 0 1200 742" role="img" aria-label="Red band over a faint photograph of a desk with laptop and papers">
  <defs>
    <linearGradient id="expFill" x1="0" y1="0" x2="1" y2="1">
      <stop offset="0" stop-color="#e4242b"/><stop offset=".6" stop-color="#dc2329"/><stop offset="1" stop-color="#c91c22"/>
    </linearGradient>
  </defs>
  <polygon points="0,0 600,60 1200,0 1200,658 600,742 0,658" fill="url(#expFill)"/>
  <line x1="600" y1="83" x2="600" y2="742" stroke="#fff" stroke-width="4"/>
  <g fill="var(--red)" stroke="#fff" stroke-width="3">
    <circle cx="600" cy="83" r="8"/><circle cx="600" cy="298" r="8"/><circle cx="600" cy="433" r="8"/><circle cx="600" cy="595" r="8"/>
  </g>
  <g fill="#fff">
    <circle cx="480" cy="187" r="52"/><circle cx="700" cy="300" r="52"/><circle cx="480" cy="435" r="52"/><circle cx="717" cy="580" r="52"/>
  </g>
  <g fill="none" stroke="#fff" stroke-width="2" stroke-dasharray="2 3">
    <circle cx="480" cy="187" r="58"/><circle cx="700" cy="300" r="58"/><circle cx="480" cy="435" r="58"/><circle cx="717" cy="580" r="58"/>
  </g>
  <!-- laptop -->
  <g fill="none" stroke="var(--red)" stroke-width="3">
    <rect x="464" y="172" width="32" height="22" rx="2"/>
    <path d="M456 200 h48 l-4 5 h-40 z" fill="var(--red)"/>
  </g>
  <!-- code brackets -->
  <g fill="none" stroke="var(--red)" stroke-width="4" stroke-linecap="round">
    <polyline points="688,286 676,300 688,314"/><polyline points="712,286 724,300 712,314"/>
  </g>
  <!-- institution -->
  <g fill="var(--red)">
    <polygon points="480,417 458,429 502,429"/>
    <rect x="460" y="432" width="40" height="3"/>
    <rect x="463" y="437" width="5" height="14"/><rect x="472" y="437" width="5" height="14"/><rect x="483" y="437" width="5" height="14"/><rect x="492" y="437" width="5" height="14"/>
    <rect x="458" y="452" width="44" height="4"/>
  </g>
  <!-- briefcase -->
  <g fill="var(--red)">
    <rect x="699" y="569" width="36" height="26" rx="3"/>
    <rect x="709" y="562" width="16" height="9" rx="2" fill="none" stroke="var(--red)" stroke-width="3"/>
  </g>
</svg>
<h2 class="red-title" style="top:910px">MY<br>EXPERIENCE</h2>

<div class="timeline-item left" style="left:143px;top:1060px">
  <div class="item-title">Vendora Market</div>
  <div class="item-role">Web Developer&nbsp; 2012 - 2015</div>
  <div class="item-text">Lorem ipsum dolor sit amet, consectetur adipiscing elit, sed do eiusmod tempor incididunt ut labore et dolore magna aliqua. Ut enim ad minim veniam</div>
</div>
<div class="timeline-item right" style="left:800px;top:1168px">
  <div class="item-title">Northwind Soft</div>
  <div class="item-role">Web Developer&nbsp; 2012 - 2015</div>
  <div class="item-text">Lorem ipsum dolor sit amet, consectetur adipiscing elit, sed do eiusmod tempor incididunt ut labore et dolore magna aliqua. Ut enim ad minim veniam</div>
</div>
<div class="timeline-item left" style="left:143px;top:1299px">
  <div class="item-title">Ashford - Master of Art</div>
  <div class="item-role">Web Developer&nbsp; 2012 - 2015</div>
  <div class="item-text">Lorem ipsum dolor sit amet, consectetur adipiscing elit, sed do eiusmod tempor incididunt ut labore et dolore magna aliqua. Ut enim ad minim veniam</div>
</div>
<div class="timeline-item right" style="left:800px;top:1486px">
  <div class="item-role" style="margin-top:0">Outsourcing&nbsp; 2012 - 2015</div>
  <div class="item-text">Lorem ipsum dolor sit amet, consectetur adipiscing elit, sed do eiusmod tempor incididunt ut labore et dolore magna aliqua. Ut enim ad minim veniam</div>
</div>

<div class="load-more">
  <svg width="16" height="16" viewBox="0 0 16 16"><g stroke="#bbb" stroke-width="2" stroke-linecap="round"><line x1="8" y1="1" x2="8" y2="4"/><line x1="8" y1="12" x2="8" y2="15"/><line x1="1" y1="8" x2="4" y2="8"/><line x1="12" y1="8" x2="15" y2="8"/><line x1="3" y1="3" x2="5" y2="5"/><line x1="11" y1="11" x2="13" y2="13"/><line x1="3" y1="13" x2="5" y2="11"/></g></svg>
  Load more
</div>

<!-- certifications -->
<h2 class="section-title" style="top:1776px;font-size:40px">CERTIFICATIONS</h2>
<p class="intro" style="top:1836px">Bright Forge builds and maintains web shops, websites and apps, and also takes care of hosting and outsourcing. With more than ten years of hands-on experience your project is in good hands. Software is built with Scrum, so you stay involved and always know what you get.</p>
<div class="cert-badge" style="left:270px;width:136px"></div>
<div class="cert-badge" style="left:444px;width:160px"></div>
<div class="cert-badge" style="left:638px;width:112px"></div>
<div class="cert-badge" style="left:786px;width:140px"></div>

<!-- skills -->
<svg class="band" style="top:2064px" width="1200" height="530" viewBox="0 0 1200 530" role="img" aria-label="Red band over a faint city skyline">
  <polygon points="0,0 600,68 1200,0 1200,451 600,530 0,451" fill="#e4242b"/>
  <rect x="0" y="300" width="1200" height="151" fill="#d21f26" opacity=".5"/>
</svg>
<h2 class="red-title" style="top:2040px">MY<br>SKILLS</h2>

<svg class="abs" style="left:0;top:2254px" width="1200" height="130" viewBox="0 0 1200 130">
  <g fill="none" stroke-width="12">
    <circle cx="203" cy="65" r="53" stroke="#7a7a7a"/>
    <circle cx="203" cy="65" r="53" stroke="#fff" stroke-dasharray="300 333" transform="rotate(-90 203 65)"/>
    <circle cx="469" cy="65" r="53" stroke="#7a7a7a"/>
    <circle cx="469" cy="65" r="53" stroke="#fff" stroke-dasharray="266 333" transform="rotate(-90 469 65)"/>
    <circle cx="735" cy="65" r="53" stroke="#7a7a7a"/>
    <circle cx="735" cy="65" r="53" stroke="#fff" stroke-dasharray="300 333" transform="rotate(-90 735 65)"/>
    <circle cx="1000" cy="65" r="53" stroke="#7a7a7a"/>
    <circle cx="1000" cy="65" r="53" stroke="#fff" stroke-dasharray="167 333" transform="rotate(-90 1000 65)"/>
  </g>
  <g fill="#fff" font-family="Raleway, sans-serif" font-weight="600" text-anchor="middle">
    <text x="203" y="76" font-size="30">90<tspan font-size="16">%</tspan></text>
    <text x="469" y="76" font-size="30">80<tspan font-size="16">%</tspan></text>
    <text x="735" y="76" font-size="30">90<tspan font-size="16">%</tspan></text>
    <text x="1000" y="76" font-size="30">50<tspan font-size="16">%</tspan></text>
  </g>
</svg>
<div class="skill" style="left:83px;top:2358px"><div class="skill-name">Development</div><div class="skill-text">Lorem ipsum dolor sit amet, conse adipisc ing elit, sed do eiusmod tempor incididunt ut labore et dolore</div></div>
<div class="skill" style="left:349px;top:2358px"><div class="skill-name">Outsourcing</div><div class="skill-text">Lorem ipsum dolor sit amet, conse adipisc ing elit, sed do eiusmod tempor incididunt ut labore et dolore</div></div>
<div class="skill" style="left:615px;top:2358px"><div class="skill-name">Hosting</div><div class="skill-text">Lorem ipsum dolor sit amet, conse adipisc ing elit, sed do eiusmod tempor incididunt ut labore et dolore</div></div>
<div class="skill" style="left:880px;top:2358px"><div class="skill-name">Development</div><div class="skill-text">Lorem ipsum dolor sit amet, conse adipisc ing elit, sed do eiusmod tempor incididunt ut labore et dolore</div></div>

<!-- contact -->
<h2 class="section-title" style="top:2703px">Contact Us</h2>
<div class="contact-item" style="left:255px">
  <span class="contact-dot"><svg width="14" height="18" viewBox="0 0 14 18"><path d="M7 0a7 7 0 0 0-7 7c0 5 7 11 7 11s7-6 7-11a7 7 0 0 0-7-7z" fill="#fff"/><circle cx="7" cy="7" r="2.5" fill="#111"/></svg></span>
  <span>48 Maple Row, Suite B-4<br>Brookfield, OR 97201</span>
</div>
<div class="contact-item" style="left:510px">
  <span class="contact-dot"><svg width="16" height="16" viewBox="0 0 16 16"><path d="M3 1l3 3-2 2c1 2 3 4 5 5l2-2 3 3-2 3C7 15 1 9 0 3z" fill="#fff"/></svg></span>
  <span>Call Us :<br>(+1) 555.204.7781</span>
</div>
<div class="contact-item" style="left:762px">
  <span class="contact-dot"><svg width="16" height="12" viewBox="0 0 16 12"><rect x="0.5" y="0.5" width="15" height="11" fill="none" stroke="#fff"/><polyline points="1,1 8,7 15,1" fill="none" stroke="#fff"/></svg></span>
  <span>E - Mail :<br>info@brightforge.example</span>
</div>

<div class="field" style="top:2872px">Name :</div>
<div class="field" style="top:2925px">Email :</div>
<div class="field" style="top:2978px">Phone :</div>
<div class="field" style="top:3031px">Subject :</div>
<div class="field message">Message :</div>
<div class="submit">submit now</div>

<!-- footer -->
<footer class="footer"></footer>
<div class="social"><span></span><span></span><span></span><span></span><span></span></div>
<ul class="footer-nav">
  <li>HOME</li><li>ABOUT US</li><li>MY EXPERIENCE</li><li>CERTIFICATIONS</li><li>SKILLS</li><li>CONTACT US</li>
</ul>
<p class="copyright">2016 © Copyrights Bright Forge.All Rights Reserved</p>

</body>
</html>
```